Numbrella : This is a Puzzle and This is not a Puzzle

Numbrella is a new addictive way to play Sudoku (see description on the attached document).
We would like your help in developing a design for the playscreen of the game (a mock-up is in the attached document)
The winner will be entrusted with the work of the complete design of the application (home screen, configuration screen, etc.) in a specific contract.
Thank you from Paris France.
Best.
Anselme

```html
<!DOCTYPE html>
<html lang="en">
<head>
<meta charset="utf-8">
<title>Numbrella – Play Screen</title>
<link rel="stylesheet" href="https://fonts.googleapis.com/css2?family=Poppins:wght@400;500;600;700&display=swap">
<style>
:root{
  --backdrop:#c6c6c6;
  --splash-top:#e0952e;
  --splash-bottom:#e7b13c;
  --panel:#ffffff;
  --tool-bg:#f0f0f0;
  --board-bg:#f3f3f3;
  --ink:#111111;
  --white:#ffffff;
  --accent:#e8a02c;
  --star:#f0a030;
  --p1-bg:#fcd4f3;--p1:#e600c8;
  --p2-bg:#d2f8fb;--p2:#19c9dc;
  --c-blue:#0a0aa0;--c-cyan:#00ffff;--c-gold:#c8940a;--c-red:#ff0000;
  --c-silver:#c0c0c0;--c-black:#000000;--c-magenta:#ff00ff;--c-yellow:#ffff00;
  --c-green:#00ff00;--c-orange:#ffa500;--c-teal:#00d5d5;--c-indigo:#3535c8;--c-lime:#33ff33;
}
*{box-sizing:border-box;margin:0;padding:0}
html,body{width:1200px;height:638px;overflow:hidden;background:var(--backdrop)}
body{font-family:"Poppins",sans-serif;color:var(--ink)}
.stage{position:absolute;left:0;top:0;width:1400px;height:744px;transform:scale(.857143);transform-origin:0 0}
.splash{position:absolute;left:137px;top:107px;width:243px;height:525px;border-radius:34px;
  background:linear-gradient(160deg,var(--splash-top),var(--splash-bottom))}
.splash-brand{position:absolute;left:0;right:0;top:316px;display:flex;justify-content:center;align-items:center;gap:10px}
.splash-brand .mark{width:30px;height:30px;border-radius:6px;background:var(--white)}
.splash-brand .name{font-weight:700;font-size:30px;color:var(--white);line-height:1}
.playscreen{position:absolute;left:433px;top:94px;width:800px;height:375px;background:var(--panel)}
.abs{position:absolute}
.player{position:absolute;left:95px;width:86px;height:22px;border-radius:11px;display:flex;align-items:center;gap:6px;padding-left:4px}
.player .avatar{width:16px;height:16px;border-radius:50%;display:flex;align-items:center;justify-content:center}
.player .stars{color:var(--star);font-size:9px;letter-spacing:1px}
.player.p1{top:30px;background:var(--p1-bg)}.player.p1 .avatar{background:var(--p1)}
.player.p2{top:58px;background:var(--p2-bg)}.player.p2 .avatar{background:var(--p2)}
.toolbar{position:absolute;width:86px;background:var(--tool-bg)}
.toolbar.left{left:97px;top:91px;height:252px}
.toolbar.right{left:632px;top:30px;height:314px}
.tool{position:absolute;left:0;width:100%;display:flex;flex-direction:column;align-items:center;text-align:center}
.tool .icon{width:24px;height:24px;border-radius:50%;background:var(--white);display:flex;align-items:center;justify-content:center}
.tool .icon.filled{background:var(--accent)}
.tool .label{font-size:10px;font-weight:500;line-height:15px;margin-top:2px}
.color-key{position:absolute;left:203px;width:30px}
.key-cell{height:30px;font-size:10px;font-weight:600;display:flex;align-items:flex-end;padding:0 0 2px 4px}
.board{position:absolute;left:252px;top:30px;width:316px;height:314px;background:var(--board-bg)}
.blocks{position:absolute;left:18px;top:18px;display:grid;grid-template-columns:repeat(3,90px);gap:5px}
.block{display:grid;grid-template-columns:repeat(3,30px);grid-auto-rows:30px}
.cell{display:flex;align-items:center;justify-content:center;font-size:20px;font-weight:700;line-height:1}
.lt{color:var(--white)}.gy{color:#c8c8c8}
.bg-blue{background:var(--c-blue)}.bg-cyan{background:var(--c-cyan)}.bg-gold{background:var(--c-gold)}
.bg-red{background:var(--c-red)}.bg-silver{background:var(--c-silver)}.bg-black{background:var(--c-black)}
.bg-magenta{background:var(--c-magenta)}.bg-yellow{background:var(--c-yellow)}.bg-green{background:var(--c-green)}
.bg-orange{background:var(--c-orange)}.bg-teal{background:var(--c-teal)}.bg-indigo{background:var(--c-indigo)}.bg-lime{background:var(--c-lime)}
.number-key{position:absolute;left:586px;width:30px;border:1px solid var(--ink)}
.num-cell{height:29.3px;border-bottom:1px solid var(--ink);display:flex;align-items:flex-end;justify-content:center;gap:1px;padding-bottom:2px}
.num-cell:last-child{border-bottom:none}
.num-cell small{font-size:10px;font-weight:600;line-height:1}
.num-cell b{font-size:17px;font-weight:600;line-height:1}
</style>
</head>
<body>
<div class="stage">
  <section class="splash" role="img" aria-label="Splash screen with warm orange swirl background">
    <div class="splash-brand"><span class="mark"></span><span class="name">Numbrella</span></div>
  </section>

  <main class="playscreen">
    <div class="player p1"><span class="avatar"><svg width="10" height="10" viewBox="0 0 10 10"><circle cx="5" cy="3.2" r="2.2" fill="#fff"/><path d="M1 10a4 4 0 0 1 8 0z" fill="#fff"/></svg></span><span class="stars">★★★★★</span></div>
    <div class="player p2"><span class="avatar" style="background:#111"><svg width="10" height="10" viewBox="0 0 10 10"><circle cx="5" cy="3.2" r="2.2" fill="#2cd"/><path d="M1 10a4 4 0 0 1 8 0z" fill="#2cd"/></svg></span><span class="stars">★★★★</span></div>

    <aside class="toolbar left">
      <div class="tool" style="top:19px"><span class="icon filled"><svg width="12" height="12" viewBox="0 0 12 12"><path d="M10 6H2M5 3 2 6l3 3" stroke="#fff" stroke-width="1.4" fill="none"/></svg></span><span class="label">Go Back</span></div>
      <div class="tool" style="top:70px"><span class="icon"><svg width="14" height="14" viewBox="0 0 14 14"><circle cx="4" cy="4" r="2.6" fill="#e8a02c"/><circle cx="10" cy="4" r="2.6" fill="#e8a02c"/><circle cx="4" cy="10" r="2.6" fill="#e8a02c"/><circle cx="10" cy="10" r="2.6" fill="#e8a02c"/></svg></span><span class="label">Color grid<br>Only</span></div>
      <div class="tool" style="top:140px"><span class="icon"><svg width="14" height="14" viewBox="0 0 14 14"><path d="M2 8 7 3l4 4-5 5z" fill="none" stroke="#e8a02c" stroke-width="1.3"/><circle cx="10" cy="11" r="2.5" fill="#e600c8"/></svg></span><span class="label">Color Eraser</span></div>
      <div class="tool" style="top:193px"><span class="icon"><svg width="14" height="14" viewBox="0 0 14 14"><circle cx="7" cy="7" r="5.5" fill="none" stroke="#e8a02c" stroke-width="1.2"/><text x="7" y="10" font-size="8" text-anchor="middle" fill="#e8a02c" font-family="Poppins,sans-serif">?</text></svg></span><span class="label" style="margin-top:6px">Color Help</span></div>
    </aside>

    <div class="color-key" style="top:48px"><div class="key-cell bg-yellow">4</div><div class="key-cell bg-magenta">6</div><div class="key-cell bg-gold">6</div></div>
    <div class="color-key" style="top:143px"><div class="key-cell bg-red">4</div><div class="key-cell bg-orange">8</div><div class="key-cell bg-blue lt">4</div></div>
    <div class="color-key" style="top:238px"><div class="key-cell bg-lime">5</div><div class="key-cell bg-cyan">7</div><div class="key-cell bg-black lt">3</div></div>

    <section class="board">
      <div class="blocks">
        <div class="block">
          <div class="cell bg-blue lt">9</div><div class="cell bg-cyan lt">1</div><div class="cell bg-gold">5</div>
          <div class="cell bg-silver">7</div><div class="cell bg-black lt">4</div><div class="cell bg-magenta">6</div>
          <div class="cell bg-red">8</div><div class="cell bg-green">2</div><div class="cell bg-yellow">3</div>
        </div>
        <div class="block">
          <div class="cell bg-red">7</div><div class="cell bg-silver">2</div><div class="cell bg-black lt">3</div>
          <div class="cell bg-cyan">8</div><div class="cell bg-green">1</div><div class="cell bg-yellow">5</div>
          <div class="cell bg-magenta">9</div><div class="cell bg-gold">6</div><div class="cell bg-blue lt">4</div>
        </div>
        <div class="block">
          <div class="cell bg-magenta">8</div><div class="cell bg-yellow">4</div><div class="cell bg-green">6</div>
          <div class="cell bg-red">9</div><div class="cell bg-blue">2</div><div class="cell bg-gold">3</div>
          <div class="cell bg-teal">7</div><div class="cell bg-silver">5</div><div class="cell bg-black lt">1</div>
        </div>
        <div class="block">
          <div class="cell bg-cyan">5</div><div class="cell bg-red">3</div><div class="cell bg-indigo lt">1</div>
          <div class="cell bg-magenta">4</div><div class="cell bg-silver">6</div><div class="cell bg-black lt">7</div>
          <div class="cell bg-yellow">2</div><div class="cell bg-gold">9</div><div class="cell bg-green">9</div>
        </div>
        <div class="block">
          <div class="cell bg-gold">4</div><div class="cell bg-black lt">8</div><div class="cell bg-magenta">2</div>
          <div class="cell bg-yellow">1</div><div class="cell bg-red">5</div><div class="cell bg-green">9</div>
          <div class="cell bg-silver">3</div><div class="cell bg-blue lt">7</div><div class="cell bg-cyan">6</div>
        </div>
        <div class="block">
          <div class="cell bg-yellow">6</div><div class="cell bg-green">7</div><div class="cell bg-silver">9</div>
          <div class="cell bg-blue lt">3</div><div class="cell bg-gold">8</div><div class="cell bg-cyan">2</div>
          <div class="cell bg-black lt">5</div><div class="cell bg-magenta">1</div><div class="cell bg-red">4</div>
        </div>
        <div class="block">
          <div class="cell bg-black lt">6</div><div class="cell bg-indigo gy">8</div><div class="cell bg-silver">4</div>
          <div class="cell bg-gold">1</div><div class="cell bg-yellow">7</div><div class="cell bg-cyan">9</div>
          <div class="cell bg-green">3</div><div class="cell bg-magenta">5</div><div class="cell bg-red">2</div>
        </div>
        <div class="block">
          <div class="cell bg-green">5</div><div class="cell bg-yellow">9</div><div class="cell bg-red">1</div>
          <div class="cell bg-black lt">2</div><div class="cell bg-magenta">3</div><div class="cell bg-silver">8</div>
          <div class="cell bg-blue lt">6</div><div class="cell bg-cyan">4</div><div class="cell bg-gold">7</div>
        </div>
        <div class="block">
          <div class="cell bg-gold">2</div><div class="cell bg-cyan">3</div><div class="cell bg-magenta">7</div>
          <div class="cell bg-green">4</div><div class="cell bg-red">6</div><div class="cell bg-blue lt">5</div>
          <div class="cell bg-silver">1</div><div class="cell bg-black lt">9</div><div class="cell bg-yellow">8</div>
        </div>
      </div>
    </section>

    <div class="number-key" style="top:47px"><div class="num-cell"><small>9</small><b>1</b></div><div class="num-cell"><small>8</small><b>2</b></div><div class="num-cell"><small>7</small><b>3</b></div></div>
    <div class="number-key" style="top:142px"><div class="num-cell"><small>9</small><b>4</b></div><div class="num-cell"><small>8</small><b>5</b></div><div class="num-cell"><small>7</small><b>6</b></div></div>
    <div class="number-key" style="top:236px"><div class="num-cell"><small>9</small><b>7</b></div><div class="num-cell"><small>8</small><b>8</b></div><div class="num-cell"><small>7</small><b>9</b></div></div>

    <aside class="toolbar right">
      <div class="tool" style="top:8px"><span class="icon filled"><svg width="12" height="12" viewBox="0 0 12 12"><path d="M1 6 6 1.5 11 6M2.5 5v5.5h7V5" fill="#fff"/></svg></span><span class="label">Home</span></div>
      <div class="tool" style="top:55px"><span class="icon"><svg width="14" height="14" viewBox="0 0 14 14"><circle cx="7" cy="8" r="4.6" fill="none" stroke="#111" stroke-width="1.2"/><path d="M7 8V5.5M5.5 2h3" stroke="#111" stroke-width="1.2"/><circle cx="10" cy="11" r="2" fill="#e8a02c"/></svg></span><span class="label">Chrono</span></div>
      <div class="tool" style="top:104px"><span class="icon"><svg width="12" height="12" viewBox="0 0 12 12"><path d="M3 3l3 3-3 3M6 3l3 3-3 3" stroke="#e8a02c" stroke-width="1.2" fill="none"/></svg></span><span class="label" style="margin-top:6px">Go Forward</span></div>
      <div class="tool" style="top:154px"><span class="icon"><svg width="16" height="16" viewBox="0 0 16 16"><circle cx="5" cy="5" r="2.5" fill="none" stroke="#e600c8"/><circle cx="11" cy="5" r="2.5" fill="none" stroke="#19c919"/><circle cx="5" cy="11" r="2.5" fill="none" stroke="#19c9dc"/><circle cx="11" cy="11" r="2.5" fill="none" stroke="#e600c8"/></svg></span><span class="label">Number grid<br>Only</span></div>
      <div class="tool" style="top:216px"><span class="icon"><svg width="14" height="14" viewBox="0 0 14 14"><path d="M2 8 7 3l4 4-5 5z" fill="none" stroke="#e8a02c" stroke-width="1.3"/><circle cx="10" cy="11" r="2.5" fill="#e600c8"/></svg></span><span class="label">Number Eraser</span></div>
      <div class="tool" style="top:266px"><span class="icon"><svg width="14" height="14" viewBox="0 0 14 14"><circle cx="7" cy="7" r="5.5" fill="none" stroke="#e8a02c" stroke-width="1.2"/><text x="7" y="10" font-size="8" text-anchor="middle" fill="#e8a02c" font-family="Poppins,sans-serif">?</text></svg></span><span class="label">Number Help</span></div>
    </aside>
  </main>
</div>
</body>
</html>
```